Online Psychiatry business - Business Card

I need a business card design. The target audience is busy professionals of any field (this therapy appeals best to 24-35 year olds). It involves psychiatry by tele-medicine (or video-conference). Nothing on it should be a giveaway that it's about mental health. Professional design with silver or gold as the primary colors appeals to me. The card must be as simple and as uncluttered as possible. Some color and flowing design on the edge of the card appeals to me.
CrestMindLink.com should probably appear in the center of the card and stand out, i.e. bold lettering, and easy to read, no cursive, but Ariel Black. Some where below this, should appear "Too Busy to Take Care of Yourself? Think again." Since this isn't office based, I don't think an office address is necessary and limits clutter.
Information that does need to appear is my name: Gerald Whitcombe, MD
General phone number: 541-876-2209. I'm hoping to get an 24-hour answering service soon so leave a little room for this. In addition I want to include two email addresses:
CrestMindLink@maildrop-box.com and CrestMind247@maildrop-box.com
Updates

I like the designs. I would like someone to put the website in bold in the center

 as most have been doing with a smaller font reminder nearby saying "No time" etc.
but I'd like to put my name down in the corner with the rest of the contact material.
Black print against a white or grey background appeals to me, with darker silver artwork near the sides (simple abstract, like wavy lines or something you can one up with that works. 
thanks

I ve tried to provide as much feedback as possible given my time limits, so if you have extra questions, please feel free to email. I tried to attach a file of a business card I really like but make be difficult to actually manufacture. I'm going to send you a link to the photo. The card has a pull tab. There is not much information on the outside. In fact, if you were to design the outside, I would just print : Too Busy to Take Care of Yourself? Think Again.

When you pull the tab the remaining information is on the bottom half of the card. Please don't use the color pink!!!!
http://www.layoutgallerypost.com/2009/05/100-clever-card-ideas/
It is the 39th photo on the list, about 2/3ds of the way down the page. It is titled: Faltenkästli

#7 and #16 have an appeal to me, except for the dot patterns
Hope this helps

I'm running out of time and energy. I 've been trying to give do down the list and give  individual feedback but I won't be able to do that anymore.

So if you have any specific questions, write me, and again thank you for all your effort!!

I know i received your files, including your zip files, Plonix,

but Gideon, did you send me the files including ZIP on project 5914386?
thanks

Target Market(s)

Working professionals and executive, attorneys, etc.

Industry/Entity Type

Business

Logo Text

Don't Have Time to Take Care of Yourself? Think Again.

Logo styles of interest
Pictorial/Combination Logo
Wordmark Logo
Other font styles liked:
• Ariel Black appeals to me the most

Requirements
Must have
• Want to emphasize that the website must be obvious, easily found (The CrestMindLink.com)
For that reason i'd like the card to be white, and minimal decoration on one or both sides just to add some style and color
Nice to have
• A Very uncluttered, elegant design, and something that makes it stick in your head-doesn't everyone want the last?
Should not have
• Nothing on the card that give it away that this is about psychiatry, such as brain or other symbol, but also nothing that gives it away as a medical business, such as a stethoscope or red cross or anything.

```html
<!DOCTYPE html>
<html lang="en">
<head>
<meta charset="utf-8">
<title>CrestMindLink – Business Card</title>
<link rel="stylesheet" href="https://fonts.googleapis.com/css2?family=Arimo:wght@400;700&display=swap">
<style>
  :root {
    --backdrop: #e9e9e7;
    --card-silver: #8d8d8d;
    --card-edge: #7c7c7c;
    --peach: #f5c08c;
    --peach-edge: #d9a46f;
    --ink-on-peach: #6f6f6f;
    --stitch: #a9a9a9;
  }
  * { margin: 0; padding: 0; box-sizing: border-box; }
  html, body {
    width: 1200px; height: 1000px; overflow: hidden;
    background: var(--backdrop);
    font-family: "Arimo", Arial, sans-serif;
  }
  .card {
    position: absolute;
    left: 232px;
    width: 735px; height: 420px;
    background: var(--card-silver);
    border-radius: 4px;
    box-shadow: 0 10px 28px rgba(0,0,0,.22);
    overflow: hidden;
  }
  .card--outside { top: 50px; }
  .card--inside { top: 530px; }
  .card-art { position: absolute; inset: 0; width: 100%; height: 100%; }
  .tagline {
    position: absolute;
    font-size: 26px;
    color: var(--peach);
    white-space: nowrap;
  }
  .tagline strong { font-weight: 700; }
  .card--outside .tagline { left: 150px; top: 212px; }
  .card--inside .tagline { left: 150px; top: 128px; }
  .pull-label {
    position: absolute;
    left: 12px; top: 322px;
    font-size: 10px;
    letter-spacing: 1px;
    color: var(--ink-on-peach);
    transform: rotate(90deg);
    transform-origin: left top;
  }
  .contact-name {
    position: absolute;
    left: 70px; top: 232px;
    font-size: 24px; font-weight: 700;
    letter-spacing: 1px;
    text-transform: uppercase;
    color: var(--ink-on-peach);
  }
  .contact-phone {
    position: absolute;
    left: 118px; top: 280px;
    display: flex; align-items: center; gap: 10px;
    font-size: 20px; font-weight: 700;
    color: var(--ink-on-peach);
  }
  .hours-badge {
    display: inline-flex; align-items: center; justify-content: center;
    width: 30px; height: 30px;
    border: 1.5px solid var(--ink-on-peach);
    border-radius: 50%;
    font-size: 10px; font-weight: 400;
  }
  .contact-online {
    position: absolute;
    left: 410px; top: 206px;
    color: var(--ink-on-peach);
  }
  .contact-website { font-size: 22px; font-weight: 700; margin-bottom: 6px; }
  .contact-email { font-size: 16px; line-height: 1.35; }
</style>
</head>
<body>

<section class="card card--outside" aria-label="Card outside with pull tab">
  <svg class="card-art" viewBox="0 0 735 420" aria-hidden="true">
    <path d="M0,250 C40,255 70,285 72,335 C70,385 40,415 0,420 Z" fill="var(--peach)"/>
    <path d="M0,250 C40,255 70,285 72,335 C70,385 40,415 0,420" fill="none" stroke="var(--peach-edge)" stroke-width="1"/>
    <line x1="0" y1="150" x2="735" y2="150" stroke="var(--stitch)" stroke-width="1.5" stroke-dasharray="8 6"/>
    <line x1="80" y1="300" x2="735" y2="300" stroke="var(--stitch)" stroke-width="1.5" stroke-dasharray="8 6"/>
  </svg>
  <p class="tagline">Too Busy to Take Care of Yourself? <strong>Think again.</strong></p>
  <span class="pull-label">PULL</span>
</section>

<section class="card card--inside" aria-label="Card inside with contact details">
  <svg class="card-art" viewBox="0 0 735 420" aria-hidden="true">
    <path d="M0,300 C0,235 60,190 140,190 L735,190 L735,330 L210,330 C158,330 120,368 120,420 L0,420 Z" fill="var(--peach)"/>
    <path d="M0,300 C0,235 60,190 140,190 L735,190" fill="none" stroke="var(--card-edge)" stroke-width="2" stroke-dasharray="5 3"/>
    <path d="M735,330 L210,330 C158,330 120,368 120,420" fill="none" stroke="var(--card-edge)" stroke-width="2" stroke-dasharray="5 3"/>
  </svg>
  <p class="tagline">Too Busy to Take Care of Yourself? <strong>Think again.</strong></p>
  <p class="contact-name">Gerald Whitcombe, MD</p>
  <p class="contact-phone">call 541-876-2209 <span class="hours-badge">24h</span></p>
  <div class="contact-online">
    <p class="contact-website">CrestMindLink.com</p>
    <p class="contact-email">CrestMind247@maildrop-box.com</p>
    <p class="contact-email">CrestMindLink@maildrop-box.com</p>
  </div>
</section>

</body>
</html>
```